Lantern Capital Business Card Design Project

We have recently rebranded and would like to design new business cards that incorporate the corporate logo - double sided cards with corporate logo on one side and contact details on the other

Target Market(s)

Sophisticated and high net worth investors and finance industry professionals

Industry/Entity Type

Funds Management

Contact Information for Business Card

The card should prominently feature the company name and logo. Other details will be standard contact details for each staff member - name, address, phone, email, website

Colors
0054AA
0677BA
7BADD7
CADEEF
E8F1F8

Requirements
Must have
• Double-sided design with one side prominently featuring the corporate logo and the other side with all standard contact details

```html
<!DOCTYPE html>
<html lang="en">
<head>
<meta charset="utf-8">
<title>Lantern Capital – Business Card</title>
<link href="https://fonts.googleapis.com/css2?family=Tinos:wght@700&family=Arimo:wght@400&display=swap" rel="stylesheet">
<style>
  :root {
    --backdrop: #9a9a9a;
    --navy: #17467a;
    --white: #ffffff;
    --ink: #2b2b2b;
  }
  * { margin: 0; padding: 0; box-sizing: border-box; }
  html, body { width: 1200px; height: 1059px; overflow: hidden; }
  body { background: var(--backdrop); position: relative; font-family: "Arimo", Arial, sans-serif; }

  .card {
    position: absolute;
    left: 255px;
    width: 690px;
    height: 392px;
    border-radius: 18px;
    overflow: hidden;
  }
  .card--front { top: 89px; background: var(--white); }
  .card--back { top: 569px; background: var(--navy); }

  .brand {
    font-family: "Arimo", Arial, sans-serif;
    font-weight: 400;
    letter-spacing: 2px;
    white-space: nowrap;
    line-height: 1;
  }
  .card--front .brand-mark {
    position: absolute;
    left: 327px; top: 64px;
    width: 36px; height: 36px;
    border-radius: 50%;
    background: var(--navy);
  }
  .card--front .brand {
    position: absolute;
    left: 0; right: 0; top: 124px;
    text-align: center;
    font-size: 34px;
    color: var(--navy);
  }

  .person {
    position: absolute;
    right: 373px; top: 226px;
    text-align: right;
  }
  .person__name {
    font-family: "Tinos", "Times New Roman", serif;
    font-weight: 700;
    font-size: 24px;
    letter-spacing: 0.5px;
    color: var(--navy);
    line-height: 1.05;
  }
  .person__role { font-size: 16px; color: var(--ink); margin-top: 2px; }

  .divider {
    position: absolute;
    left: 344px; top: 218px;
    width: 1.5px; height: 65px;
    background: var(--navy);
  }

  .contacts { position: absolute; left: 369px; top: 211px; list-style: none; }
  .contacts li {
    display: flex; align-items: center;
    height: 25.5px;
    font-size: 16.5px; color: var(--ink);
  }
  .contacts svg { width: 14px; height: 14px; margin-right: 9px; fill: var(--navy); flex: none; }

  .address-band {
    position: absolute;
    left: 0; right: 0; top: 324px;
    height: 33px;
    background: var(--navy);
    color: var(--white);
    font-size: 16px;
    display: flex; align-items: center; justify-content: center;
  }

  .card--back .brand-row {
    position: absolute;
    left: 74px; top: 170px;
    display: flex; align-items: center; gap: 22px;
  }
  .card--back .brand-mark {
    width: 44px; height: 44px; border-radius: 50%; background: var(--white);
  }
  .card--back .brand { font-size: 44px; color: var(--white); }
</style>
</head>
<body>

<section class="card card--front" aria-label="Business card front">
  <div class="brand-mark"></div>
  <div class="brand">Lantern Capital</div>

  <div class="person">
    <div class="person__name">DANIEL HALE</div>
    <div class="person__role">CEO/Founder</div>
  </div>
  <div class="divider"></div>

  <ul class="contacts">
    <li>
      <svg viewBox="0 0 24 24" aria-hidden="true"><path d="M6.6 10.8a15.1 15.1 0 0 0 6.6 6.6l2.2-2.2a1 1 0 0 1 1-.25 11.4 11.4 0 0 0 3.6.57 1 1 0 0 1 1 1V20a1 1 0 0 1-1 1A17 17 0 0 1 3 4a1 1 0 0 1 1-1h3.5a1 1 0 0 1 1 1c0 1.25.2 2.45.57 3.6a1 1 0 0 1-.25 1z"/></svg>
      (555) 214-7390
    </li>
    <li>
      <svg viewBox="0 0 24 24" aria-hidden="true"><path d="M2 5h20v3l-10 6L2 8z M2 10l10 6 10-6v9H2z"/></svg>
      info@lanterncapital.com
    </li>
    <li>
      <svg viewBox="0 0 24 24" aria-hidden="true"><path d="M12 2a10 10 0 1 0 0 20 10 10 0 0 0 0-20zm0 2c.9 0 2.2 1.8 2.8 5H9.2C9.8 5.8 11.1 4 12 4zM4.3 9h2.9a18 18 0 0 0 0 6H4.3a8 8 0 0 1 0-6zm4.9 6a16 16 0 0 1 0-6h5.6a16 16 0 0 1 0 6zm7.6 0a18 18 0 0 0 0-6h2.9a8 8 0 0 1 0 6zM12 20c-.9 0-2.2-1.8-2.8-5h5.6c-.6 3.2-1.9 5-2.8 5z"/></svg>
      www.lanterncapital.com
    </li>
  </ul>

  <div class="address-band">Po Box 4127 Harbour Street Westfield AB 3910</div>
</section>

<section class="card card--back" aria-label="Business card back">
  <div class="brand-row">
    <div class="brand-mark"></div>
    <div class="brand">Lantern Capital</div>
  </div>
</section>

</body>
</html>
```